Law Firm Folder with 5 step inserts

Square Corners Two Pocket Presentation Folder - inside and outside design with 5 stepped inserts. Please look at website brevardclaimslaw .com for colors

Target Market(s)

Given to new clients

Industry/Entity Type

legal

Requirements
Must have
• use brand colors.
Nice to have
• would like to include partner photos
Should not have
• not generic

```html
<!DOCTYPE html>
<html lang="en">
<head>
<meta charset="UTF-8">
<title>Hale &amp; Brevard – Presentation Folder</title>
<link href="https://fonts.googleapis.com/css2?family=Cinzel:wght@500;600&family=Montserrat:wght@400;600;700&family=Playfair+Display:wght@500&display=swap" rel="stylesheet">
<style>
  :root {
    --navy: #13213c;
    --navy-deep: #0c1629;
    --gold: #c9a24a;
    --gold-light: #e0c27a;
    --paper: #ffffff;
    --mist: #eef0f3;
    --ink: #3a4150;
    --stage: #ffffff;
  }
  * { box-sizing: border-box; margin: 0; padding: 0; }
  html, body { width: 1200px; height: 2208px; overflow: hidden; background: var(--stage); }
  body { font-family: "Montserrat", Arial, sans-serif; color: var(--ink); position: relative; }

  .spread {
    position: absolute; left: 40px; width: 1120px; height: 700px;
    display: flex; box-shadow: 0 6px 24px rgba(0,0,0,.12);
  }
  .spread--inside { top: 364px; }
  .spread--outside { top: 1144px; }
  .panel { position: relative; width: 560px; height: 700px; overflow: hidden; }

  /* brand lockup */
  .brand { display: flex; flex-direction: column; align-items: center; }
  .brand__mark { width: 54px; height: 54px; border-radius: 50%; border: 2px solid var(--gold); margin-bottom: 12px; }
  .brand__name { font-family: "Cinzel", Georgia, serif; font-weight: 600; font-size: 28px; letter-spacing: 2px; color: var(--navy); }
  .brand__tag { font-family: "Cinzel", Georgia, serif; font-weight: 500; font-size: 12px; letter-spacing: 3px; color: var(--gold); margin-top: 4px; }
  .brand--light .brand__name { color: var(--paper); }

  /* inside left */
  .inside-left { background: var(--mist); }
  .inside-left__texture { position: absolute; inset: 0 0 280px 0; background: linear-gradient(135deg, #f7f8fa, #e3e6eb); }
  .inside-left .brand { position: absolute; top: 110px; left: 0; right: 0; }
  .pocket {
    position: absolute; left: 0; right: 0; bottom: 0; background: var(--navy);
    border-top: 4px solid var(--gold);
  }
  .inside-left .pocket { height: 290px; clip-path: polygon(0 8%, 88% 8%, 100% 0, 100% 100%, 0 100%); border: none; padding: 60px 40px 0; }
  .pocket__title { font-weight: 700; font-size: 19px; color: var(--paper); margin-bottom: 14px; }
  .pocket__copy { font-size: 11px; line-height: 1.65; color: #c8cfdc; margin-bottom: 10px; }

  /* inside right */
  .inside-right { background: var(--paper); }
  .inside-right__intro { position: absolute; left: 34px; top: 190px; width: 220px; font-size: 10.5px; line-height: 1.65; color: var(--ink); }
  .tabs { position: absolute; right: 0; top: 0; width: 280px; }
  .tab { height: 44px; display: flex; align-items: center; padding-left: 22px; font-weight: 600; font-size: 13px; color: var(--paper); }
  .tab--gold { background: var(--gold); }
  .tab--navy { background: var(--navy); }
  .inside-right .pocket { height: 300px; }
  .seal { position: absolute; left: 50px; top: 70px; width: 104px; height: 104px; border-radius: 50%; background: radial-gradient(circle, var(--gold-light), var(--gold)); }
  .guarantees { position: absolute; left: 186px; top: 78px; right: 34px; }
  .guarantees__title { font-weight: 700; font-size: 17px; color: var(--gold); margin-bottom: 12px; }
  .guarantees__item { display: flex; gap: 8px; font-size: 11px; line-height: 1.5; color: var(--paper); margin-bottom: 8px; }
  .guarantees__item svg { flex: none; margin-top: 2px; }

  /* outside back */
  .back-cover { background: var(--paper); }
  .back-cover .brand { position: absolute; top: 40px; left: 0; right: 0; }
  .back-cover__photo { position: absolute; left: 0; right: 0; top: 190px; height: 210px; background: linear-gradient(180deg, #f1f2f5 0%, #c7ccd6 60%, #56617a 100%); }
  .back-cover__band { position: absolute; left: 0; right: 0; bottom: 0; height: 300px; background: var(--navy); padding: 36px 44px 0; }
  .back-cover__title { font-weight: 700; font-size: 18px; line-height: 1.35; color: var(--gold); text-transform: uppercase; margin-bottom: 14px; }
  .back-cover__copy { font-size: 11px; line-height: 1.65; color: #c8cfdc; margin-bottom: 18px; }
  .contact { font-weight: 700; font-size: 15px; color: var(--paper); margin-bottom: 4px; }
  .contact--web { font-weight: 400; font-size: 11px; color: #c8cfdc; margin-bottom: 14px; }
  .social { display: flex; gap: 10px; }
  .social span { width: 20px; height: 20px; border-radius: 50%; background: var(--gold); }

  /* outside front */
  .front-cover { background: var(--navy-deep); }
  .front-cover .brand { position: absolute; top: 70px; left: 0; right: 0; }
  .front-cover__photo { position: absolute; left: 0; right: 0; top: 230px; height: 260px; background: linear-gradient(120deg, #1d3563 0%, #3d6aa8 45%, #9ab3d6 70%, #2a4778 100%); border-top: 3px solid var(--gold); border-bottom: 3px solid var(--gold); }
  .front-cover__tagline { position: absolute; left: 0; right: 0; top: 545px; text-align: center; font-family: "Playfair Display", Georgia, serif; font-weight: 500; font-size: 26px; line-height: 1.4; letter-spacing: 1px; color: var(--gold); text-transform: uppercase; }
</style>
</head>
<body>

<section class="spread spread--inside">
  <div class="panel inside-left">
    <div class="inside-left__texture" role="img" aria-label="Subtle light grey geometric pattern background"></div>
    <div class="brand">
      <span class="brand__mark"></span>
      <span class="brand__name">HALE &amp; BREVARD</span>
      <span class="brand__tag">PERSONAL INJURY LAW</span>
    </div>
    <div class="pocket">
      <h2 class="pocket__title">Talk to A Florida Personal Injury Lawyer Today</h2>
      <p class="pocket__copy">If you were hurt because of someone else's carelessness, our team is here to guide you through every step. We handle the insurers, gather the evidence and fight for the full recovery you deserve.</p>
      <p class="pocket__copy">From the first call to the final settlement, we keep you informed and put your recovery first.</p>
    </div>
  </div>

  <div class="panel inside-right">
    <p class="inside-right__intro">Our team has helped injured families across Florida recover what they lost. Use the tabs at right to learn about our services, our attorneys and how we can help you move forward.</p>
    <nav class="tabs">
      <div class="tab tab--gold">Practice Areas</div>
      <div class="tab tab--navy">Our Attorneys</div>
      <div class="tab tab--gold">Client Stories</div>
      <div class="tab tab--navy">Locations</div>
      <div class="tab tab--gold">We Can Help</div>
    </nav>
    <div class="pocket">
      <div class="seal"></div>
      <div class="guarantees">
        <h3 class="guarantees__title">Our Guarantees</h3>
        <p class="guarantees__item"><svg width="12" height="12" viewBox="0 0 12 12"><path d="M1 6l3 3 7-7" fill="none" stroke="#c9a24a" stroke-width="2"/></svg>No fee unless we win your case.</p>
        <p class="guarantees__item"><svg width="12" height="12" viewBox="0 0 12 12"><path d="M1 6l3 3 7-7" fill="none" stroke="#c9a24a" stroke-width="2"/></svg>We return every call within one business day.</p>
        <p class="guarantees__item"><svg width="12" height="12" viewBox="0 0 12 12"><path d="M1 6l3 3 7-7" fill="none" stroke="#c9a24a" stroke-width="2"/></svg>You work directly with an experienced attorney.</p>
      </div>
    </div>
  </div>
</section>

<section class="spread spread--outside">
  <div class="panel back-cover">
    <div class="brand">
      <span class="brand__mark"></span>
      <span class="brand__name">HALE &amp; BREVARD</span>
      <span class="brand__tag">PERSONAL INJURY LAW</span>
    </div>
    <div class="back-cover__photo" role="img" aria-label="Portrait of the two founding partners in suits"></div>
    <div class="back-cover__band">
      <h2 class="back-cover__title">Talk to a Florida Personal<br>Injury Lawyer Today</h2>
      <p class="back-cover__copy">If you or a loved one was injured, you do not have to face the insurance company alone. Our attorneys offer a free case review and will explain your options in plain language.</p>
      <p class="contact">(555) 014-2290</p>
      <p class="contact contact--web">brevardclaimslaw.com</p>
      <div class="social"><span></span><span></span><span></span><span></span></div>
    </div>
  </div>

  <div class="panel front-cover">
    <div class="brand brand--light">
      <span class="brand__mark"></span>
      <span class="brand__name">HALE &amp; BREVARD</span>
      <span class="brand__tag">PERSONAL INJURY LAW</span>
    </div>
    <div class="front-cover__photo" role="img" aria-label="Handshake in front of a blue city skyline"></div>
    <p class="front-cover__tagline">It's not just a case.<br>It's your life.</p>
  </div>
</section>

</body>
</html>
```